Bright Crest Lifts

im looking for someone to help me with my letterhead design. i have already got my logo design just need help with this part

Industry/Entity Type

Construction

Colors
0255a3

Requirements
Must have
• must have all my details eg. bank details, abn and acn

```html
<!DOCTYPE html>
<html lang="en">
<head>
<meta charset="utf-8">
<title>Bright Crest Lifts — Letterhead</title>
<link href="https://fonts.googleapis.com/css2?family=Open+Sans:wght@400;700&display=swap" rel="stylesheet">
<style>
  :root {
    --backdrop: #ababab;
    --paper: #ffffff;
    --brand-blue: #0255a3;
    --ink: #1b1b1b;
    --footer-ink: #4a4a4a;
  }
  * { margin: 0; padding: 0; box-sizing: border-box; }
  html, body {
    width: 1200px;
    height: 1200px;
    overflow: hidden;
    background: var(--backdrop);
  }
  body {
    display: flex;
    align-items: center;
    justify-content: center;
    font-family: "Open Sans", Arial, sans-serif;
  }
  .letterhead {
    position: relative;
    width: 800px;
    height: 1120px;
    background: var(--paper);
    box-shadow: 0 6px 18px rgba(0, 0, 0, 0.25);
  }
  .letterhead__brand {
    position: absolute;
    top: 78px;
    left: 0;
    right: 0;
    display: flex;
    align-items: center;
    justify-content: center;
    gap: 14px;
  }
  .brand__square {
    width: 30px;
    height: 30px;
    background: var(--brand-blue);
  }
  .brand__name {
    font-weight: 700;
    font-size: 34px;
    letter-spacing: 1px;
    color: var(--ink);
  }
  .letterhead__rule {
    position: absolute;
    left: 70px;
    right: 70px;
    top: 930px;
    height: 3px;
    background: var(--brand-blue);
  }
  .letterhead__footer {
    position: absolute;
    top: 952px;
    left: 0;
    right: 0;
    text-align: center;
    font-size: 12.5px;
    line-height: 1.45;
    color: var(--footer-ink);
  }
</style>
</head>
<body>
  <main class="letterhead">
    <header class="letterhead__brand">
      <span class="brand__square" aria-hidden="true"></span>
      <span class="brand__name">Bright Crest Lifts</span>
    </header>

    <div class="letterhead__rule"></div>

    <footer class="letterhead__footer">
      <p>Bright Crest Lifts | ABN 00 000 000 000 | AFSL and Australian Credit Licence 000000</p>
      <p>000 Harbour Lane Sydney NSW Australia 0000 | GPO Box 0000 Sydney NSW Australia 2001</p>
      <p>Bank account: 00000000-00000000-00000000 | Bank swift: BCLXAU2S000</p>
      <p>Phone +61 0 0000 0000 | Fax +61 0 0000 0000 | Email: info@brightcrestlifts.net | Web: brightcrestlifts.net</p>
    </footer>
  </main>
</body>
</html>
```